Business card logo/design needed

I need a new and fresh business card to get my name out there.
I have made plenty before and have a logo but I dont think it is sending the right message across.
I am a personal trainer running a small online business designed to cut the cost of training by taking it online, allowing you to purchase training over the net, through the help of Skype and video uploads.
You can personalized programs hand written for you or more general programs aimed at your goals.
Our goal is to get everyone to look like and behave like an athlete because there is no point in being in shape if you cant do anything with that body.
I also have a strong background in sports, having played low level college basketball in america and worked as a strength and conditioning coach. I dont like running or slow cardio, I am more focused on weights and functional training for aerobic fitness.
I am young for what I do, but I have lot of knowledge and I need something that says that I am not your standard drill sergeant trainer but someone who will truly help you reach your goals.
My curent logo text is "the climb to the top" but I am not set on that.

Industry/Entity Type

Personal Trainer

Contact Information for Business Card

Desmond Quilby
Summit Forge Motion
Personal trainer
Strength and conditioning coach
0481 552 709
www.summitforgemotion.example

```html
<!DOCTYPE html>
<html lang="en">
<head>
<meta charset="utf-8">
<title>Summit Forge Motion – Business Card</title>
<link href="https://fonts.googleapis.com/css2?family=Josefin+Sans:wght@300;400;600&family=Marcellus&display=swap" rel="stylesheet">
<style>
  :root {
    --page-bg: #3a3532;
    --card-black: #0b0b0b;
    --card-glow: #232323;
    --brand-green: #8cc63f;
    --text-white: #f2f2f2;
    --text-grey: #c9c9c9;
    --skin-light: #a86a45;
    --skin-dark: #5a3420;
  }
  * { box-sizing: border-box; margin: 0; padding: 0; }
  html, body {
    width: 1200px; height: 1000px; overflow: hidden;
    background: var(--page-bg);
  }
  .sheet {
    position: relative; width: 1200px; height: 1000px;
    display: flex; flex-direction: column; align-items: center;
    justify-content: center; gap: 50px;
  }
  .card {
    position: relative; width: 800px; height: 433px; overflow: hidden;
    background: radial-gradient(ellipse at 50% 40%, var(--card-glow) 0%, var(--card-black) 70%);
    box-shadow: 0 10px 30px rgba(0,0,0,0.45);
  }

  /* Front */
  .card-front {
    display: flex; flex-direction: column; align-items: center; justify-content: center;
  }
  .brand-dot {
    width: 46px; height: 46px; border-radius: 50%;
    background: var(--brand-green); margin-bottom: 26px;
  }
  .brand-name {
    font-family: "Marcellus", serif; font-size: 27px; letter-spacing: 0.5px;
    text-transform: uppercase; color: var(--brand-green); line-height: 1;
  }
  .brand-tagline {
    margin-top: 7px;
    font-family: "Josefin Sans", sans-serif; font-weight: 600; font-size: 12px;
    letter-spacing: 2.6px; text-transform: uppercase; color: var(--text-grey);
  }

  /* Back */
  .athlete-photo {
    position: absolute; left: 0; top: 0; width: 330px; height: 100%;
    background:
      linear-gradient(90deg, rgba(11,11,11,0) 55%, var(--card-black) 100%),
      radial-gradient(ellipse at 40% 55%, var(--skin-light) 0%, var(--skin-dark) 60%, #1a0f09 100%);
  }
  .role-headline {
    position: absolute; left: 258px; top: 56px;
    font-family: "Josefin Sans", sans-serif; font-weight: 300; font-size: 31px;
    color: var(--text-white); white-space: nowrap;
  }
  .contact {
    position: absolute; left: 435px; top: 238px;
    font-family: "Josefin Sans", sans-serif;
  }
  .contact-name {
    font-family: "Marcellus", serif; font-size: 41px; color: var(--brand-green); line-height: 1;
  }
  .contact-title {
    margin-top: 6px; font-weight: 600; font-size: 12px; letter-spacing: 2.6px;
    text-transform: uppercase; color: var(--text-grey);
  }
  .contact-label {
    margin-top: 18px; font-size: 15px; color: var(--brand-green);
  }
  .contact-label + .contact-value { margin-top: 5px; }
  .contact-value {
    font-size: 17px; color: var(--text-white);
  }
  .contact-label.web { margin-top: 10px; }
</style>
</head>
<body>
  <main class="sheet">
    <section class="card card-front" aria-label="Card front">
      <span class="brand-dot"></span>
      <h1 class="brand-name">Summit Forge Motion</h1>
      <p class="brand-tagline">The climb to the top</p>
    </section>

    <section class="card card-back" aria-label="Card back">
      <div class="athlete-photo" role="img" aria-label="Photo of an athlete's bare muscular chest and shoulder"></div>
      <p class="role-headline">Strength and conditioning coach</p>
      <div class="contact">
        <h2 class="contact-name">Desmond Quilby</h2>
        <p class="contact-title">Personal trainer</p>
        <p class="contact-label">Phone:</p>
        <p class="contact-value">0481 552 709</p>
        <p class="contact-label web">Web:</p>
        <p class="contact-value">www.summitforgemotion.example</p>
      </div>
    </section>
  </main>
</body>
</html>
```